Fennick Executive Search - New Business Card Design Project

We are an executive search firm called Fennick Executive Search based in the UK. We require a custom design for a business card. We're looking to convey a professional service to executives for executive search recruitment services. In terms of colours, we like dark blues and grays (maybe even silver incorporated somewhere if we go for a foiled type of card) but we're open to your artistic flare. See our current logo in attachments. We are totally open on design so long as the design is slick and professional.
Updates

Thanks for all your contributions of various designs. I have to say the quality of work has been amazing which is going to make our job quite difficult in the coming days on making a decision. Thanks to you all that have taken the time to submit designs thus far. We'll keep on reviewing and try to narrow down our selection as soon as possible.

Target Market(s)

Executive Search

Industry/Entity Type

Recruitment

Contact Information for Business Card

Fennick Executive Search,
Exclusively Sourcing & Hiring Senior Leaders
Gordon Pellbury, Managing Director,
07823 906417
0117 486 7132
gordon@fennickexecutive.co.uk
fennickexecutive.co.uk
58 Lindmoor Court, Hatherley Road, Bristol, BS32 9QJ

Font styles to use
Sans Serif
Other font styles liked:
• Roboto (which is used in our logo)

Requirements
Must have
• Our logo (It has a subtle fade on it from #02071d at top to #333649 at bottom)
• The logo can be on one side or both sides
• Must be elegant and professional
• We have 2nd slogan CONSULT | INSPIRE | INNOVATE | DELIVER which can be incorporated into the card
Nice to have
• Use of blues and grey colours
• Compatible with similar styling to our website fennickexecutive.co.uk
Should not have
• Must not be overly brash
• Must not contain cartoon characters

```html
<!DOCTYPE html>
<html lang="en">
<head>
<meta charset="UTF-8">
<title>Fennick Executive Search – Business Card</title>
<link href="https://fonts.googleapis.com/css2?family=Roboto:wght@400;500;700&display=swap" rel="stylesheet">
<style>
  :root {
    --stage: #3b3b3e;
    --navy-top: #02071d;
    --navy-bottom: #333649;
    --navy-ink: #1c2040;
    --paper: #ffffff;
    --grey-text: #5a5c66;
    --body-text: #15172a;
    --light: #f4f5f8;
  }
  * { margin: 0; padding: 0; box-sizing: border-box; }
  html, body {
    width: 1200px; height: 800px; overflow: hidden;
    background: var(--stage);
    font-family: "Roboto", Arial, sans-serif;
  }
  .stage {
    width: 1200px; height: 800px;
    display: flex; align-items: center; justify-content: center; gap: 40px;
  }
  .card {
    width: 540px; height: 309px; position: relative;
    box-shadow: 0 10px 28px rgba(0,0,0,.35);
  }

  /* Brand name placeholder */
  .brand { display: flex; align-items: center; gap: 12px; font-weight: 500; line-height: 1; white-space: nowrap; }
  .brand__mark { width: 18px; height: 18px; background: currentColor; flex: none; }

  /* Front */
  .card--front { background: var(--paper); color: var(--body-text); }
  .card--front .brand { position: absolute; left: 34px; top: 38px; font-size: 24px; color: var(--navy-ink); }
  .tagline { position: absolute; left: 34px; top: 76px; font-size: 13px; color: var(--grey-text); letter-spacing: .2px; }
  .person { position: absolute; left: 34px; top: 196px; }
  .person__name { font-size: 18px; font-weight: 700; color: var(--navy-ink); letter-spacing: .4px; text-transform: uppercase; }
  .person__role { font-size: 14px; margin-top: 3px; }
  .contact { position: absolute; left: 292px; top: 168px; font-size: 13.5px; line-height: 1.35; }
  .contact__address { margin-bottom: 10px; }
  .contact__list { list-style: none; }
  .contact__item { display: flex; align-items: center; gap: 10px; height: 19px; }
  .contact__icon { width: 12px; height: 12px; fill: var(--navy-ink); flex: none; }

  /* Back */
  .card--back {
    background: linear-gradient(180deg, var(--navy-top), var(--navy-bottom));
    color: var(--light);
    display: flex; flex-direction: column; align-items: center; justify-content: center;
  }
  .card--back .brand { font-size: 30px; color: var(--light); }
  .card--back .brand__mark { width: 22px; height: 22px; }
  .slogan { margin-top: 40px; font-size: 12px; letter-spacing: 2px; font-weight: 400; }
  .slogan__divider { padding: 0 6px; opacity: .8; }
</style>
</head>
<body>
<main class="stage">
  <section class="card card--front">
    <div class="brand"><span class="brand__mark"></span><span class="brand__name">Fennick Executive Search</span></div>
    <p class="tagline">Exclusively Sourcing &amp; Hiring Senior Leaders</p>

    <div class="person">
      <p class="person__name">Gordon Pellbury</p>
      <p class="person__role">Managing Director</p>
    </div>

    <div class="contact">
      <p class="contact__address">58 Lindmoor Court, Hatherley Road<br>Bristol, BS32 9QJ</p>
      <ul class="contact__list">
        <li class="contact__item">
          <svg class="contact__icon" viewBox="0 0 24 24"><path d="M6.6 10.8a15.1 15.1 0 0 0 6.6 6.6l2.2-2.2c.3-.3.7-.4 1-.2 1.1.4 2.3.6 3.6.6.6 0 1 .4 1 1V20c0 .6-.4 1-1 1C10.6 21 3 13.4 3 4c0-.6.4-1 1-1h3.5c.6 0 1 .4 1 1 0 1.3.2 2.5.6 3.6.1.3 0 .7-.2 1z"/></svg>
          <span>07823 906417</span>
        </li>
        <li class="contact__item">
          <svg class="contact__icon" viewBox="0 0 24 24"><path d="M6 2h12v5H6zM4 8h16a2 2 0 0 1 2 2v7h-4v5H6v-5H2v-7a2 2 0 0 1 2-2zm4 8v4h8v-4z"/></svg>
          <span>0117 486 7132</span>
        </li>
        <li class="contact__item">
          <svg class="contact__icon" viewBox="0 0 24 24"><path d="M2 5h20v14H2zm2 2v.5l8 5 8-5V7z"/></svg>
          <span>gordon@fennickexecutive.co.uk</span>
        </li>
        <li class="contact__item">
          <svg class="contact__icon" viewBox="0 0 24 24"><path d="M12 2a10 10 0 1 0 0 20 10 10 0 0 0 0-20zm6.9 9h-3a15 15 0 0 0-1.3-6A8 8 0 0 1 18.9 11zM12 4.1c.9 1.3 1.7 3.7 1.9 6.9h-3.8c.2-3.2 1-5.6 1.9-6.9zM9.4 5a15 15 0 0 0-1.3 6h-3A8 8 0 0 1 9.4 5zm-4.3 8h3a15 15 0 0 0 1.3 6A8 8 0 0 1 5.1 13zm6.9 6.9c-.9-1.3-1.700-3.7-1.900-6.9h3.8c-.2 3.2-1 5.6-1.9 6.9zm2.6-.9a15 15 0 0 0 1.3-6h3a8 8 0 0 1-4.3 6z"/></svg>
          <span>www.fennickexecutive.co.uk</span>
        </li>
      </ul>
    </div>
  </section>

  <section class="card card--back">
    <div class="brand"><span class="brand__mark"></span><span class="brand__name">Fennick Executive Search</span></div>
    <p class="slogan">CONSULT<span class="slogan__divider">|</span>INSPIRE<span class="slogan__divider">|</span>INNOVATE<span class="slogan__divider">|</span>DELIVER</p>
  </section>
</main>
</body>
</html>
```